business card for law firm that reflects the web site -www.MarlaQuentby.com. That is pleasant to read

We need a business card for a small law firm. Your company designed our logo - tree of life - which I can provide to the designers. The card should be on both sides. Use the coloring from the web site (www.MarlaQuentby.com) and logo (I have several formats). I am attaching the logo, but not sure what format to use.

First side name of firm: Law Office of M.K. Quentby, P.A. 4819 West Pallisor, Suite 300, Phoenix, AZ 85016, Phone: 602.555.3841, Fax: 602.555.7290, web site: www.MarlaQuentby.com, email: MQuentby@MarlaQuentby.com.
Marla K. Quentby Bankruptcy and Foreclosure Attorney & Counselor.
Back side (perhaps vertical) the logo and then Notes with lines. At the bottom: Proud to help people and small businesses file for bankruptcy protection. We are a debt relief agency.
Updates

I have several versions of the logo. Will be happy to share whatever you need. Added Sunday, April 3, 2016

Target Market(s)

everyone

Industry/Entity Type

Legal

Contact Information for Business Card

I prefer something unique (rounded edges, design that adopts my web site - www.MarlaQuentby.com.

Font styles to use
Serif

Requirements
Must have
• First side name of firm: Law Office of M.K. Quentby, P.A. 4819 West Pallisor, Suite 300, Phoenix, AZ 85016, Phone: 602.555.3841, Fax: 602.555.7290, web site: www.MarlaQuentby.com, email: MQuentby@MarlaQuentby.com.
• Marla K. Quentby Bankruptcy and Foreclosure Attorney & Counselor.
• Back side (perhaps vertical) the logo and then Notes with lines. At the bottom: Proud to help people and small businesses file for bankruptcy protection. We are a debt relief agency.
• Green and brown colors that reflect the web site: www.MarlaQuentby.com
Should not have
• Type so small that older people cannot read.

```html
<!DOCTYPE html>
<html lang="en">
<head>
<meta charset="utf-8">
<title>Law Office of M.K. Quentby, P.A. — Business Card</title>
<link href="https://fonts.googleapis.com/css2?family=PT+Sans:wght@400;700&display=swap" rel="stylesheet">
<style>
  :root {
    --page: #f3f3f2;
    --leaf-dark: #3f6b2a;
    --leaf-mid: #6f9a45;
    --leaf-light: #a9c783;
    --lawn: #5f9a3a;
    --mist: rgba(226, 232, 222, 0.62);
    --bark: #3b2119;
    --cream: #f3ede2;
    --ink: #3a2418;
    --rule: #f1efe9;
  }
  * { margin: 0; padding: 0; box-sizing: border-box; }
  html, body { width: 1088px; height: 1200px; overflow: hidden; background: var(--page); }
  body { position: relative; font-family: "PT Sans", sans-serif; }

  .card {
    position: absolute; left: 188px; width: 712px; height: 456px;
    overflow: hidden; box-shadow: 0 3px 10px rgba(0,0,0,0.18);
  }
  .card--front { top: 110px; }
  .card--back { top: 624px; }

  .scenery {
    position: absolute; inset: 0;
    background: linear-gradient(180deg, var(--leaf-dark) 0%, var(--leaf-mid) 30%, var(--leaf-light) 55%, var(--leaf-mid) 78%, var(--lawn) 100%);
  }

  .mist { position: absolute; left: 0; right: 0; background: var(--mist); }
  .rule { position: absolute; left: 0; right: 0; background: var(--rule); }

  .seal {
    position: absolute; border-radius: 50%;
    background: var(--cream); display: flex; align-items: center; justify-content: center;
    color: var(--ink); font-weight: 700; text-align: center;
  }

  /* front */
  .front__title { position: absolute; left: 259px; top: 64px; font-size: 30px; color: var(--ink); white-space: nowrap; }
  .front__panel { position: absolute; left: 0; right: 0; top: 133px; height: 207px; background: var(--bark); }
  .front__divider { position: absolute; left: 216px; top: 0; bottom: 0; width: 1px; background: rgba(243,237,226,0.35); }
  .front__seal { left: 15px; top: 17px; width: 184px; height: 184px; font-size: 22px; }
  .address { position: absolute; right: 519px; top: 113px; text-align: right; color: var(--cream); font-size: 17px; line-height: 25px; }
  .address__zip { display: flex; align-items: flex-end; justify-content: flex-end; gap: 8px; }
  .address__zip svg { width: 44px; height: 38px; }
  .person { position: absolute; left: 262px; top: 10px; color: var(--cream); }
  .person__name { font-size: 30px; line-height: 40px; }
  .person__role { font-size: 17px; margin-top: 2px; white-space: nowrap; }
  .contacts { position: absolute; left: 250px; top: 92px; color: var(--cream); list-style: none; }
  .contacts li { display: flex; align-items: center; gap: 16px; height: 40px; font-size: 24px; white-space: nowrap; }
  .contacts li.contacts__email { font-size: 21px; }
  .contacts svg { width: 26px; height: 24px; flex: none; }
  .front__web { position: absolute; left: 259px; top: 359px; font-size: 28px; font-weight: 700; color: var(--ink); display: flex; align-items: center; gap: 4px; }
  .front__web svg { width: 32px; height: 32px; }

  /* back */
  .back__seal { left: 426px; top: 29px; width: 258px; height: 258px; font-size: 30px; }
  .back__message { position: absolute; left: 57px; top: 222px; color: var(--ink); font-size: 26px; line-height: 35px; text-transform: uppercase; }
  .back__web { position: absolute; left: 62px; top: 385px; font-size: 29px; color: var(--cream); display: flex; align-items: center; gap: 4px; }
  .back__web svg { width: 32px; height: 32px; }
</style>
</head>
<body>

<section class="card card--front">
  <div class="scenery" role="img" aria-label="Photograph of an oak-lined avenue with a path running through green lawn"></div>
  <div class="mist" style="top:50px;height:60px"></div>
  <div class="rule" style="top:122px;height:4px"></div>
  <h1 class="front__title">Law Office of M.K. Quentby, P.A.</h1>

  <div class="front__panel">
    <div class="front__divider"></div>
    <address class="address">
      <div class="address__zip">
        <svg viewBox="0 0 44 38"><path d="M22 3 L3 20 h6 v15 h10 v-10 h6 v10 h10 v-15 h6 z" fill="none" stroke="#f3ede2" stroke-width="3" stroke-linejoin="round"/></svg>
        <span>AZ 85016</span>
      </div>
      <div>4819 West Pallisor</div>
      <div>Suite 300, Phoenix</div>
    </address>

    <div class="person">
      <h2 class="person__name" style="font-weight:400">Marla Quentby</h2>
      <p class="person__role">Bankruptcy and Foreclosure Attorney &amp; Counselor.</p>
    </div>

    <ul class="contacts">
      <li>
        <svg viewBox="0 0 24 24"><path d="M6 2 l4 5 -2 3 c1 3 3 5 6 6 l3 -2 5 4 -3 4 C10 22 2 14 2 5 z" fill="#f3ede2"/></svg>
        602-555-3841
      </li>
      <li>
        <svg viewBox="0 0 26 24"><rect x="7" y="1" width="12" height="7" fill="#f3ede2"/><rect x="2" y="9" width="22" height="9" rx="2" fill="#f3ede2"/><rect x="7" y="15" width="12" height="8" fill="#f3ede2" stroke="#3b2119" stroke-width="1.5"/></svg>
        602-555-7290
      </li>
      <li class="contacts__email">
        <svg viewBox="0 0 26 24"><path d="M2 9 L13 2 L24 9 V22 H2 Z M2 9 L13 16 L24 9 M2 22 L10 14 M24 22 L16 14" fill="none" stroke="#f3ede2" stroke-width="1.8" stroke-linejoin="round"/></svg>
        MQuentby@MarlaQuentby.com.
      </li>
    </ul>
  </div>
  <div class="seal front__seal">M.K.<br>Quentby</div>

  <div class="rule" style="top:345px;height:4px"></div>
  <div class="mist" style="top:353px;height:57px"></div>
  <div class="front__web">
    <svg viewBox="0 0 32 32"><g fill="none" stroke="#3a2418" stroke-width="2"><circle cx="16" cy="16" r="13"/><ellipse cx="16" cy="16" rx="6" ry="13"/><path d="M3 16h26M5 9h22M5 23h22"/></g></svg>
    www.marlaquentby.com
  </div>
</section>

<section class="card card--back">
  <div class="scenery" role="img" aria-label="Photograph of an oak-lined avenue with a path running through green lawn"></div>
  <div class="mist" style="top:151px;height:51px"></div>
  <div class="rule" style="top:202px;height:3px"></div>
  <div class="mist" style="top:209px;height:169px"></div>
  <div class="seal back__seal">M.K.<br>Quentby</div>
  <p class="back__message">Proud to help people<br>and small businesses<br>file for bankruptcy protection<br>we are a debt relief agency</p>
  <div class="back__web">
    <svg viewBox="0 0 32 32"><g fill="none" stroke="#f3ede2" stroke-width="2"><circle cx="16" cy="16" r="13"/><ellipse cx="16" cy="16" rx="6" ry="13"/><path d="M3 16h26M5 9h22M5 23h22"/></g></svg>
    www.marlaquentby.com
  </div>
</section>

</body>
</html>
```